Real Estate Investor needs awesome business card design

I invest in real estate, focused on multi-family properties, and I need a business card to hand out to potential partners. I prefer simple, clean designs, but it needs to stand out, so I'd like there to be a bit of red in the design as well.

It should include this information:

Front
Dallin Pecksworth
Real Estate Investor
Direct phone: 502-867-3394
Email: dallinhpecksworth@quillmail.example
Headshot (Picture), I've uploaded a few, just pick the one you think looks best with your design. You can remove the background from the headshot image if it looks better.

Back
The back of the card's design should flow and be congruent with the front. On the back I want to put an inspirational quote or question. There will be different ones depending on the card, so I'll need the original file so I can edit it in the end.

For now, use “The Pessimist Sees Difficulty In Every Opportunity. The Optimist Sees The Opportunity In Every Difficulty.” -Barnaby Ellsworth

Target Market(s)

Investors

Industry/Entity Type

Real Estate

Contact Information for Business Card

Front
Dallin Pecksworth
Real Estate Investor

Back
The back of the card's design should flow and be congruent with the front. On the back I want to put an inspirational quote or question. There will be different ones depending on the card, so I'll need the original file so I can edit it in the end. I've uploaded some EXAMPLES of business cards with quotes on them. Don't copy but feel free to use them as inspiration.

The design will be printed on "ZIB sized" business cards
1039 x 697 pixels
with rounded corners

Font styles to use
Serif
Decorative
Script

Colors
ec1f27

Requirements
Must have
• Headshot, name, and other information in it.
• 1039 x 697 pixels
• Rounded corners
• Clean design that pops. I'm open to see any color background, including black.
• Headshots can be located here: https://www.filecrate.example/sh/8kd2wq7mzt31hvx/BBQTXP4ruf9LmQ0KhcvWx7b?dl=0
Nice to have
• It would be awesome if the design included a personal signature or monogram, but if not I'll get a personal logo developed later and the card redesigned if I think it needs it.
Should not have
• Cluttered design

```html
<!DOCTYPE html>
<html lang="en">
<head>
<meta charset="utf-8">
<title>Dallin Pecksworth – Business Card</title>
<link href="https://fonts.googleapis.com/css2?family=Roboto+Condensed:wght@700&family=Roboto:wght@300&display=swap" rel="stylesheet">
<style>
  :root {
    --canvas: #e4e5e7;
    --card-black: #1c1c1c;
    --band-black: #0b0b0b;
    --brand-red: #ec1f27;
    --white: #ffffff;
    --photo-light: #d9c3b4;
    --photo-dark: #2a3550;
  }
  * { margin: 0; padding: 0; box-sizing: border-box; }
  html, body { width: 1200px; height: 1000px; overflow: hidden; }
  body { background: var(--canvas); position: relative; font-family: "Roboto", sans-serif; color: var(--white); }

  .card { position: absolute; top: 348px; width: 466px; height: 266px; border-radius: 22px; overflow: hidden; }
  .card--front { left: 122px; background: var(--card-black); }
  .card--back { left: 611px; background: var(--brand-red); }

  .headshot {
    position: absolute; left: 56px; top: 50px; width: 132px; height: 132px; border-radius: 50%;
    border: 4px solid var(--brand-red);
    background: radial-gradient(circle at 50% 38%, var(--photo-light) 0 30%, #f2f2f2 31% 55%, var(--photo-dark) 56%);
  }

  .monogram {
    position: absolute; left: 270px; top: 60px; width: 122px; text-align: center;
    font-family: "Roboto Condensed", sans-serif; font-weight: 700; font-size: 50px; line-height: 1;
    color: var(--white);
  }
  .identity { position: absolute; left: 230px; top: 144px; width: 202px; text-align: center; }
  .identity__name { font-family: "Roboto Condensed", sans-serif; font-weight: 700; font-size: 18px; letter-spacing: 0.3px; line-height: 20px; }
  .identity__title { font-weight: 300; font-size: 14px; line-height: 18px; }

  .contact-band {
    position: absolute; left: 0; top: 210px; width: 100%; height: 34px; background: var(--brand-red);
    font-weight: 300; font-size: 13.5px; line-height: 34px;
  }
  .contact-band__phone { position: absolute; left: 62px; width: 120px; text-align: center; }
  .contact-band__email { position: absolute; left: 206px; width: 250px; text-align: center; }

  .quote {
    position: absolute; left: 20px; top: 72px; width: 426px; text-align: center;
    font-family: "Roboto Condensed", sans-serif; font-weight: 700; font-size: 19px; line-height: 24.5px;
  }
  .attribution-band {
    position: absolute; left: 0; top: 210px; width: 100%; height: 36px; background: var(--band-black);
  }
  .attribution-band__author {
    position: absolute; left: 0; width: 100%; text-align: center; line-height: 36px;
    font-family: "Roboto Condensed", sans-serif; font-weight: 700; font-size: 19px;
  }
  .attribution-band__monogram {
    position: absolute; right: 36px; line-height: 36px;
    font-family: "Roboto Condensed", sans-serif; font-weight: 700; font-size: 18px;
  }
</style>
</head>
<body>
  <section class="card card--front">
    <div class="headshot" role="img" aria-label="Headshot of Dallin Pecksworth"></div>
    <div class="monogram">DP</div>
    <div class="identity">
      <p class="identity__name">DALLIN PECKSWORTH</p>
      <p class="identity__title">Real Estate Investor</p>
    </div>
    <div class="contact-band">
      <span class="contact-band__phone">502-867-3394</span>
      <span class="contact-band__email">dallinhpecksworth@quillmail.example</span>
    </div>
  </section>

  <section class="card card--back">
    <p class="quote">“THE PESSIMIST SEES DIFFICULTY<br>IN EVERY OPPORTUNITY.<br>THE OPTIMIST SEES THE OPPORTUNITY<br>IN EVERY DIFFICULTY.”</p>
    <div class="attribution-band">
      <span class="attribution-band__author">-BARNABY ELLSWORTH</span>
      <span class="attribution-band__monogram">DP</span>
    </div>
  </section>
</body>
</html>
```